Kentucky residential recovery center needs a flyer design

We need a flyer design for a 16 bed male residential/inpatient recovery center based in Richmond, Kentucky. The facility provides short term (average 30 day) treatment to those struggling with substace abuse and addiction. The design should communicate trust, assurance, safety.
Our wesite provides more information https://morvalcare.org/treatment-services/residential-treatment/

Target Market(s)

Men (typically 30-50) struggling with substance addiction

```html
<!DOCTYPE html>
<html lang="en">
<head>
<meta charset="utf-8">
<title>Morval Care – Residential Recovery Center Flyer</title>
<link rel="stylesheet" href="https://fonts.googleapis.com/css2?family=Noto+Sans:wght@400;600;700;800&family=Oswald:wght@500&family=Open+Sans:ital@1&display=swap">
<style>
  :root{
    --green:#0c9a2a;
    --green-dark:#07781f;
    --navy:#12136e;
    --paper:#f1f1f0;
    --stage:#dcdcdc;
    --white:#ffffff;
    --ink-soft:#2b2b3a;
  }
  *{box-sizing:border-box;margin:0;padding:0}
  html,body{width:1200px;height:1163px;overflow:hidden;background:var(--stage)}
  body{font-family:"Noto Sans",sans-serif;position:relative}
  .flyer{position:absolute;left:204px;top:20px;width:792px;height:1123px;background:var(--paper);overflow:hidden;box-shadow:0 6px 24px rgba(0,0,0,.18)}
  .flyer-shapes{position:absolute;inset:0}

  .brand{position:absolute;left:30px;top:38px;width:160px;display:flex;flex-direction:column;align-items:center;gap:8px}
  .brand-dot{width:90px;height:90px;border-radius:50%;background:var(--navy)}
  .brand-name{font-size:20px;font-weight:700;color:var(--navy);line-height:24px;white-space:nowrap}

  .title-band{position:absolute;left:0;top:197px;width:500px;height:117px;background:var(--green);border-radius:0 58px 58px 0}
  .title-main{position:absolute;left:37px;top:196px;color:var(--white);font-size:58px;font-weight:600;line-height:60px;letter-spacing:-.5px;white-space:nowrap}
  .title-sub{position:absolute;left:38px;top:251px;color:var(--white);font-size:29px;font-weight:600;line-height:28px;white-space:nowrap}
  .room-photo{position:absolute;left:412px;top:199px;width:114px;height:114px;border-radius:50%;border:4px solid var(--white);box-shadow:0 0 0 3px var(--green);background:radial-gradient(circle at 50% 60%,#4a4440,#b9b3aa 60%,#d9d4cc)}

  .intro{position:absolute;left:39px;top:325px;font-size:22.5px;line-height:27px;color:var(--navy);white-space:nowrap}
  .intro em{font-style:normal;font-weight:700;color:var(--green)}

  .rule{position:absolute;left:36px;width:699px;height:2px;background:var(--green)}
  .issues-kicker{position:absolute;left:38px;top:546px;font-size:18.5px;font-weight:700;color:var(--green);white-space:nowrap}
  .issues-title{position:absolute;left:38px;top:576px;font-size:41px;font-weight:800;color:var(--navy);line-height:1;display:flex;align-items:center;gap:14px;white-space:nowrap}
  .issues-title svg{width:28px;height:32px}
  .issues-sub{position:absolute;left:38px;top:617px;font-size:26px;line-height:35px;color:var(--navy);white-space:nowrap}

  .issue-list{position:absolute;left:428px;top:533px;list-style:none;width:250px}
  .issue-list li{display:flex;align-items:center;gap:14px;height:35px;font-size:22.5px;line-height:26px;font-weight:600;color:var(--green);white-space:nowrap}
  .issue-list li span{display:block;width:210px;height:35px;padding-top:4px;border-bottom:1.5px dotted var(--green)}
  .issue-list li:last-child span{border-bottom:none}
  .issue-list svg{width:22px;height:22px;flex:none}

  .services{position:absolute;left:36px;top:678px;width:330px;height:349px;background:linear-gradient(180deg,var(--green),var(--green-dark));border-bottom-left-radius:40px}
  .services-head{height:44px;background:var(--navy);color:var(--white);font-size:22px;font-weight:700;line-height:44px;padding-left:12px;letter-spacing:.3px;white-space:nowrap}
  .services-list{list-style:none;padding:8px 0 0 26px;font-family:"Oswald",sans-serif;font-weight:500;font-size:18px;color:var(--white);line-height:30.7px;white-space:nowrap}
  .services-list li::before{content:"• "}

  .how-title{position:absolute;left:380px;top:681px;font-size:23.5px;font-weight:700;color:var(--green);line-height:29px}
  .thumb{position:absolute;top:682px;width:69px;height:70px;border-radius:6px;border:2px solid #e9e9e9}
  .thumb-1{left:554px;background:linear-gradient(160deg,#8e8c88,#4b3a2c)}
  .thumb-2{left:631px;background:linear-gradient(160deg,#c8c5bf,#5a4a3c)}
  .thumb-3{left:707px;background:linear-gradient(160deg,#bfb4a3,#6a5440)}

  .step{position:absolute;left:386px;display:flex;gap:9px;font-family:"Open Sans",sans-serif;font-style:italic;font-size:11px;line-height:13px;color:var(--ink-soft)}
  .step span{width:180px}
  .step svg{width:20px;height:20px;flex:none;margin-top:2px}
  .step-rule{position:absolute;left:415px;border-top:1.5px dotted var(--green)}

  .people-photo{position:absolute;left:602px;top:781px;width:190px;height:224px;background:linear-gradient(180deg,rgba(241,241,240,0) 0%,#8a7f76 25%,#5c6470 60%,#c25a5e 100%);border-top-left-radius:70px}

  .contact{position:absolute;right:21px;top:1029px;text-align:right;color:var(--white);font-style:normal}
  .contact-head{font-size:20px;font-weight:700;letter-spacing:.3px;line-height:28px}
  .contact-line{font-size:21px;line-height:29px;display:flex;justify-content:flex-end;align-items:center;gap:8px;white-space:nowrap}
  .contact-line svg{width:18px;height:18px}

  .footer-brand{position:absolute;left:14px;top:1077px;font-size:14px;font-weight:700;color:var(--white)}
</style>
</head>
<body>
<main class="flyer">
  <svg class="flyer-shapes" viewBox="0 0 792 1123" width="792" height="1123">
    <defs>
      <linearGradient id="roomTone" x1="0" y1="0" x2="1" y2="1">
        <stop offset="0" stop-color="#b3a48f"/>
        <stop offset=".5" stop-color="#6b5a48"/>
        <stop offset="1" stop-color="#2a2a2a"/>
      </linearGradient>
    </defs>
    <path role="img" aria-label="Photo of a bedroom with bunk beds in the recovery center" d="M298,0 C250,60 215,130 219,200 L252,317 C300,370 360,395 450,405 C600,420 720,470 792,560 L792,0 Z" fill="url(#roomTone)"/>
    <path d="M298,0 C250,60 215,130 219,200" fill="none" stroke="var(--green)" stroke-width="5"/>
    <path d="M252,317 C300,370 360,395 450,405 C600,420 720,470 792,560 L792,720 C770,620 700,500 560,452 C460,420 360,430 300,380 C278,362 262,342 252,317 Z" fill="var(--green)"/>
    <path d="M0,930 C40,1010 140,1055 300,1075 C420,1088 500,1060 600,1020 C680,990 740,985 792,990 L792,1123 L0,1123 Z" fill="var(--green)"/>
    <path d="M0,930 C40,1010 140,1055 300,1075 C420,1088 500,1060 600,1020 C680,990 740,985 792,990 L792,1002 C740,998 690,1000 610,1032 C510,1072 420,1098 300,1088 C140,1070 30,1020 0,955 Z" fill="var(--navy)"/>
  </svg>

  <div class="brand"><span class="brand-dot"></span><span class="brand-name">Morval Care</span></div>

  <div class="title-band"></div>
  <h1 class="title-main">16 BED MALE</h1>
  <p class="title-sub">RESIDENTIAL/INPATIENT<br>RECOVERY CENTER</p>
  <div class="room-photo" role="img" aria-label="Photo of a meeting room with an oval table and chairs"></div>

  <p class="intro">Based in Richmond,<br>Kentucky. The facility<br>provides short term<br><em>(average 30 day)</em> treatment to<br>those struggling with substace<br>abuse and addiction.</p>

  <div class="rule" style="top:529px"></div>
  <p class="issues-kicker">Problems we can help with</p>
  <h2 class="issues-title">WHAT ISSUES <svg viewBox="0 0 28 32"><path d="M0,0 L28,16 L0,32 Z" fill="var(--green)"/></svg></h2>
  <p class="issues-sub">CAN BE TREATED?</p>

  <ul class="issue-list">
    <li><svg viewBox="0 0 22 22"><path d="M9,2h4v5l2,3v10H7V10l2-3Z" fill="none" stroke="var(--navy)" stroke-width="1.5"/></svg><span>Alcoholism</span></li>
    <li><svg viewBox="0 0 22 22"><path d="M3,19L17,5M13,3l6,6M6,12l4,4M19,3l-2,2" fill="none" stroke="var(--navy)" stroke-width="1.5"/></svg><span>Drug addiction</span></li>
    <li><svg viewBox="0 0 22 22"><circle cx="6" cy="6" r="3" fill="none" stroke="var(--navy)" stroke-width="1.5"/><circle cx="15" cy="7" r="3" fill="none" stroke="var(--navy)" stroke-width="1.5"/><path d="M3,18c3-4 12-4 16,0" fill="none" stroke="var(--navy)" stroke-width="1.5"/></svg><span>Medication addiction</span></li>
    <li><svg viewBox="0 0 22 22"><path d="M5,20v-5C2,12 3,3 11,3c6,0 8,4 7,8l2,3h-2v3h-4v3" fill="none" stroke="var(--navy)" stroke-width="1.5"/></svg><span>Behavioral health</span></li>
  </ul>
  <div class="rule" style="top:672px"></div>

  <section class="services">
    <h3 class="services-head">SERVICES OFFERED BY US:</h3>
    <ul class="services-list">
      <li>OUTPATIENT</li>
      <li>INTENSIVE OUTPATIENT</li>
      <li>RESIDENTIAL</li>
      <li>TARGETED CASE MANAGEMENT</li>
      <li>PEER SUPPORT</li>
      <li>INDIVIDUAL AND GROUP THERAPY</li>
      <li>MEDICATED ASSISTED TREATMENT (‘MAT’)</li>
      <li>PHYSICIAN APPOINTMENTS</li>
      <li>TELEMEDICINE</li>
    </ul>
  </section>

  <h3 class="how-title">HOW DOES IT<br>WORK?</h3>
  <div class="thumb thumb-1" role="img" aria-label="Photo of the facility lounge"></div>
  <div class="thumb thumb-2" role="img" aria-label="Photo of a bedroom"></div>
  <div class="thumb thumb-3" role="img" aria-label="Photo of a bunk bed room"></div>

  <div class="people-photo" role="img" aria-label="Photo of two program graduates holding certificates"></div>

  <p class="step" style="top:771px"><svg viewBox="0 0 20 20"><path d="M2,3h10v7H6l-3,3v-3H2Z M9,10v3h6l3,3v-3h1V7h-4" fill="none" stroke="var(--navy)" stroke-width="1.2"/></svg><span>Speak with our team in private about the nature of your challenges and what you need help with</span></p>
  <div class="step-rule" style="top:830px;width:208px"></div>
  <p class="step" style="top:848px"><svg viewBox="0 0 20 20"><circle cx="10" cy="6" r="4" fill="none" stroke="var(--navy)" stroke-width="1.2"/><path d="M3,19c0-5 3-7 7-7s7,2 7,7" fill="none" stroke="var(--navy)" stroke-width="1.2"/></svg><span>Together we select an appropriate time slot to book you in for an in-duction appointment with one of our clinical staff</span></p>
  <div class="step-rule" style="top:915px;width:174px"></div>
  <p class="step" style="top:934px"><svg viewBox="0 0 20 20"><circle cx="10" cy="10" r="8.5" fill="none" stroke="var(--navy)" stroke-width="1.2"/><path d="M8,6l6,4-6,4Z" fill="var(--navy)"/></svg><span>Once the induction is completed, we'll schedule you in to commence your inpatient program</span></p>

  <div class="footer-brand">Morval Care</div>

  <address class="contact">
    <p class="contact-head">CONTACT US TODAY</p>
    <p class="contact-line"><svg viewBox="0 0 18 18"><circle cx="9" cy="9" r="8" fill="none" stroke="var(--navy)" stroke-width="1.3"/><path d="M6,5l2,2-1,1c1,2 2,3 3,3l1-1 2,2-1,1c-3,0-7-4-7-7Z" fill="var(--navy)"/></svg>859-555-0142</p>
    <p class="contact-line"><svg viewBox="0 0 18 18"><rect x="1" y="3.5" width="16" height="11" fill="none" stroke="var(--navy)" stroke-width="1.3"/><path d="M1,3.5l8,6 8-6" fill="none" stroke="var(--navy)" stroke-width="1.3"/></svg>admissions@morvalcare.org</p>
  </address>
</main>
</body>
</html>
```